Hearts Held High / Walk by the Shore

We are looking to design a flyer for a concert. The concert date is 9/11/2021 located at the Birchmoor Pond State Park on the Tennessee River. Can pull pics from the artist website. Dwayne Halvers opens to follow with Tall Cousin Lark and the closing with Owen Pratley.
Idea of shadowed behind a soaring eagle and incorporated with the American flag. Sponsored by at bottom - Circle of Keepers

```html
<!DOCTYPE html>
<html lang="en">
<head>
<meta charset="utf-8">
<title>Dwayne Halvers – Concert Flyer</title>
<link rel="stylesheet" href="https://fonts.googleapis.com/css2?family=Montserrat:wght@200;400;600;700;800&family=Oswald:wght@400;600&display=swap">
<style>
  :root {
    --teal-top: #0d5b72;
    --teal-mid: #0a3d4e;
    --teal-deep: #03141c;
    --gold-light: #f3dc96;
    --gold: #c9a24d;
    --gold-dark: #8f6a25;
    --ink: #1a1a1a;
    --white: #ffffff;
    --artist-tone-a: #3c4650;
    --artist-tone-b: #1b1f25;
    --ghost-tone: rgba(120, 170, 185, 0.16);
  }
  * { margin: 0; padding: 0; box-sizing: border-box; }
  html, body { width: 837px; height: 1200px; overflow: hidden; background: #d0d0d0; }
  .flyer {
    position: relative;
    width: 837px;
    height: 1200px;
    overflow: hidden;
    background: linear-gradient(180deg, var(--teal-top) 0%, var(--teal-mid) 45%, var(--teal-deep) 100%);
    font-family: "Montserrat", sans-serif;
    color: var(--white);
  }
  .artist-photo {
    position: absolute;
    inset: 0;
    width: 837px;
    height: 1200px;
  }
  .gold-text {
    background: linear-gradient(180deg, var(--gold-light) 0%, var(--gold) 45%, var(--gold-dark) 100%);
    -webkit-background-clip: text;
    background-clip: text;
    color: transparent;
  }
  .headliner {
    position: absolute;
    left: 54px;
    top: 78px;
    line-height: 1;
    font-weight: 800;
    text-transform: uppercase;
    z-index: 2;
  }
  .headliner__first { display: block; font-size: 136px; letter-spacing: 1px; }
  .headliner__last {
    display: block;
    font-size: 128px;
    margin-top: -4px;
    color: var(--white);
    text-shadow: 4px 4px 0 rgba(0, 0, 0, 0.45);
  }
  .date-label {
    position: absolute;
    left: 55px;
    top: 414px;
    font-size: 32px;
    font-weight: 700;
    letter-spacing: 0.3px;
    z-index: 2;
  }
  .date {
    position: absolute;
    left: 52px;
    top: 458px;
    z-index: 2;
  }
  .date__day {
    position: absolute;
    left: 0;
    top: 0;
    display: inline-block;
    font-family: "Oswald", sans-serif;
    font-weight: 600;
    font-size: 222px;
    line-height: 0.88;
    transform: scaleX(0.88);
    transform-origin: left top;
  }
  .date__suffix {
    position: absolute;
    left: 114px;
    top: 10px;
    white-space: nowrap;
    font-size: 78px;
    line-height: 1;
  }
  .date__suffix-th { font-family: "Oswald", sans-serif; font-weight: 400; }
  .date__suffix-month { font-weight: 700; margin-left: 12px; }
  .date__year {
    position: absolute;
    left: 112px;
    top: 76px;
    font-size: 136px;
    font-weight: 200;
    line-height: 1;
  }
  .venue-tag {
    position: absolute;
    left: 55px;
    top: 731px;
    width: 340px;
    height: 66px;
    border-radius: 12px 0 0 12px;
    background: linear-gradient(180deg, var(--gold-light) 0%, var(--gold) 55%, var(--gold-dark) 100%);
    color: var(--ink);
    font-size: 34px;
    font-weight: 700;
    padding: 11px 0 0 22px;
    z-index: 0;
  }
  .venue {
    position: absolute;
    left: 57px;
    top: 820px;
    font-size: 32px;
    font-weight: 700;
    line-height: 41px;
    z-index: 2;
  }
  .sponsor {
    position: absolute;
    left: 55px;
    top: 1050px;
    z-index: 2;
  }
  .sponsor__label { font-size: 21px; font-weight: 400; }
  .sponsor__name { font-size: 25px; font-weight: 700; margin-top: 8px; }
</style>
</head>
<body>
  <main class="flyer">
    <div class="venue-tag">located at the</div>

    <svg class="artist-photo" viewBox="0 0 837 1200" role="img" aria-label="Photo of the artist in a cap, glasses and dark hooded jacket holding a folded map, with a faint enlarged copy of the same photo behind">
      <defs>
        <linearGradient id="artistTone" x1="0" y1="0" x2="0" y2="1">
          <stop offset="0" stop-color="var(--artist-tone-a)"/>
          <stop offset="1" stop-color="var(--artist-tone-b)"/>
        </linearGradient>
      </defs>
      <path class="artist-ghost" fill="var(--ghost-tone)"
        d="M390 140 C400 55 545 35 620 85 C665 125 665 250 645 330 L565 400 L385 380 C375 300 380 215 390 140 Z"/>
      <path class="artist-figure" fill="url(#artistTone)"
        d="M540 320 C560 280 690 275 735 320 L748 370 C752 420 742 480 722 510
           C772 530 822 560 837 580 L837 1200 L420 1200
           C395 1130 330 1030 280 980 C300 880 350 790 400 720
           C440 660 500 610 560 575 C590 560 620 540 630 510
           C600 480 575 440 570 400 Z"/>
    </svg>

    <h1 class="headliner">
      <span class="headliner__first gold-text">Dwayne</span>
      <span class="headliner__last">Halvers</span>
    </h1>

    <p class="date-label">THE CONCERT DATE IS</p>
    <div class="date">
      <span class="date__day gold-text">9</span>
      <span class="date__suffix"><span class="date__suffix-th">TH</span><span class="date__suffix-month">NOV</span></span>
      <span class="date__year">2021</span>
    </div>

    <p class="venue">Birchmoor Pond<br>State Park on<br>the Tennessee<br>River</p>

    <div class="sponsor">
      <p class="sponsor__label">Sponsored by</p>
      <p class="sponsor__name">Circle of Keepers</p>
    </div>
  </main>
</body>
</html>
```